Wordpress website design for children’s entertainment agency

What is the aim of the website?

The aim for the website is to attract potential bookers and to get them to respond to the Call to action: contact the entertainer - phone call/request a call back/completing a form.
All the information needs to be easy to access and navigate to, especially on mobile view.
The call to action needs to be clear and easy to navigate.

What I need:

Critical - This website needs to look good on all devices.
Easy navigation on a mobile device is essential so the elements need to be bold and easy to click on with a thumb (when in mobile view)

The ‘grid area’ needs to be graphics based with simple descriptions, i.e. ‘magic shows’, Circus Clowns, Face painting, Costume Characters, Party Host, Carnival Parties, Balloon Sculpting, DJ and MC, Princess Parties, Holiday Parties, Fun Add Ons and Contact.

See: http://www.merrylopkin.com/
and http://tottlejoyworks.com/

I would like to see a sample page layout as well to see how your design would be carried through the site layout in the inside pages.

Target Market(s)

The site visitors are mainly mums, aged between 25 - 41. Other visitors will included event organisers looking for entertainment services for baptism, communions and sweet 16’s

Industry/Entity Type

Entertainment Industry

Number of Pages Required

1 page

Font styles to use
Sans Serif

Colors
6c459b
fbed22
0493ce

Requirements
Must have
• Critical - This website needs to look good on all devices.
• Easy navigation on a mobile device is essential so the elements need to be bold and easy to click on with a thumb (when in mobile view)
• The ‘grid area’ needs to be graphics based with simple descriptions, i.e. ‘magic shows’, Circus Clowns, Face painting, Costume Characters, Party Host, Carnival Parties, Balloon Sculpting, DJ and MC, Princess Parties, Holiday Parties, Fun Add Ons and Contact.
• See: http://www.merrylopkin.com/
• and http://tottlejoyworks.com/
Nice to have
• clean looking and fun with an element of ‘Brambo’ and stars (this is the exciting site http://quindlesplaybarn.com/index.html)

```html
<!DOCTYPE html>
<html lang="en">
<head>
<meta charset="utf-8">
<title>Quindle's Play Barn – About Us</title>
<link href="https://fonts.googleapis.com/css2?family=Luckiest+Guy&family=Lato:wght@400;700;900&display=swap" rel="stylesheet">
<style>
:root{
  --sun:#fed34a;
  --sun-deep:#fbb034;
  --orange:#f47b20;
  --purple:#4a2e7d;
  --blue:#1f6fb8;
  --star:#3c7fd1;
  --navy:#0a1f4a;
  --ink:#1b1b1b;
  --white:#ffffff;
  --panel:#fdbb4d;
}
*{margin:0;padding:0;box-sizing:border-box}
html,body{width:1200px;height:2177px;overflow:hidden;background:var(--white)}
body{position:relative;font-family:"Lato",sans-serif;color:var(--ink)}
.display{font-family:"Luckiest Guy","Lato",sans-serif;font-weight:900;text-transform:uppercase;font-synthesis:none;letter-spacing:.5px}

.hero{position:absolute;left:0;top:0;width:1200px;height:520px;
  background:radial-gradient(circle at 30% 40%,#fff3a0 0%,var(--sun) 45%,var(--sun-deep) 100%)}
.hero-photo{position:absolute;left:650px;top:0;width:550px;height:586px;
  background:linear-gradient(160deg,#f4c23d 0%,#e44a2a 45%,#2d4fb0 80%,#f0c84a 100%)}
.tagline{position:absolute;color:var(--white);font-size:46px;line-height:1;
  text-shadow:-3px 3px 0 var(--ink)}
.tagline.one{left:32px;top:28px}
.tagline.two{left:170px;top:82px}
.brand{position:absolute;left:62px;top:225px;display:flex;align-items:center;gap:14px}
.brand-dot{width:44px;height:44px;border-radius:50%;background:var(--purple)}
.brand-name{font-size:34px;color:var(--purple);line-height:1}
.cta{position:absolute;top:425px;height:54px;background:var(--white);
  box-shadow:-6px 6px 0 var(--purple);display:flex;align-items:center;justify-content:center;
  color:var(--blue);font-size:28px;line-height:1}
.cta.contact{left:31px;width:250px}
.cta.call{left:356px;width:360px}
.book-star{position:absolute;left:975px;top:-8px;width:240px;height:250px}

.main-nav{position:absolute;left:0;top:520px;width:1200px;height:66px;
  background:linear-gradient(#fafafa,#dcdcdc);border-top:3px solid #bdbdbd;
  box-shadow:0 6px 6px rgba(0,0,0,.45);
  display:flex;align-items:center;justify-content:space-between;padding:0 14px 0 18px}
.main-nav a{font-size:26px;line-height:1;color:var(--orange);text-decoration:none;
  text-shadow:-1px 1px 0 var(--purple)}
.main-nav a.current{color:var(--blue)}

.page-title{position:absolute;left:111px;width:725px;top:640px;text-align:center;
  font-size:66px;line-height:1;color:var(--orange);text-shadow:-3px 3px 0 var(--ink)}
.page-sub{position:absolute;left:60px;width:840px;top:736px;text-align:center;
  font-size:20px;line-height:1;color:var(--ink)}
.stage-photo{position:absolute;left:231px;top:797px;width:510px;height:337px;border-radius:10px;
  background:radial-gradient(ellipse at 50% 40%,#c8201e 0%,#8e0d0d 65%,#2a0707 100%)}
.about-copy{position:absolute;left:111px;top:1168px;width:730px;font-size:20.5px;line-height:28px}
.about-copy p{margin-bottom:28px}

.contact-panel{position:absolute;left:897px;top:648px;width:280px;height:497px;background:var(--panel);
  padding:22px 42px 0}
.contact-panel h2{font-size:28px;line-height:1;text-align:center;color:var(--ink);margin-bottom:24px}
.field{width:197px;height:36px;margin-bottom:20px;border-radius:12px;background:var(--white);
  box-shadow:inset 0 4px 3px rgba(0,0,0,.55);font-size:15px;color:#a9a9a9;padding:8px 14px}
.field.area{height:160px}
.submit{width:197px;height:40px;border-radius:14px;
  background:linear-gradient(#ffe08a,var(--orange));box-shadow:0 5px 4px rgba(0,0,0,.5);
  font-size:18px;text-align:center;line-height:40px;color:var(--ink)}

.social{position:absolute;left:928px;top:1208px;width:222px;display:grid;
  grid-template-columns:1fr 1fr;row-gap:34px;column-gap:14px}
.social-item{display:flex;flex-direction:column;align-items:center;gap:6px;font-size:16px;font-weight:700;color:var(--blue)}
.social-item .dot{width:72px;height:72px;border-radius:50%;background:var(--blue)}

.site-footer{position:absolute;left:0;top:2058px;width:1200px;height:119px;
  background:linear-gradient(#5d8dd0 0%,#123a7c 35%,var(--navy) 100%);color:var(--white);font-size:21px}
.site-footer .item{position:absolute;top:46px;display:flex;align-items:center;gap:12px}
</style>
</head>
<body>

<header class="hero">
  <div class="hero-photo" role="img" aria-label="Photo of a clown in a red and yellow striped costume with blue hair and a red top hat"></div>
  <div class="tagline one display">Award Winning</div>
  <div class="tagline two display">Family Entertainment</div>
  <div class="brand"><span class="brand-dot"></span><span class="brand-name display">Quindle's Play Barn</span></div>
  <a class="cta contact display">Contact Us</a>
  <a class="cta call display">Call 555-014-2277</a>
  <svg class="book-star" viewBox="0 0 230 240" aria-label="Book your party today">
    <polygon points="115,6 145,86 228,90 162,143 186,228 115,180 44,228 68,143 2,90 85,86" fill="#3c7fd1" stroke="#ffffff" stroke-width="6"/>
    <g transform="rotate(15 115 124)" font-family="Luckiest Guy, Lato, sans-serif" font-weight="900" font-size="19" fill="#fed34a" text-anchor="middle" style="font-synthesis:none">
      <text x="115" y="102">BOOK</text>
      <text x="115" y="126">YOUR PARTY</text>
      <text x="115" y="150">TODAY</text>
    </g>
  </svg>
</header>

<nav class="main-nav display">
  <a>Home</a><a class="current">About</a><a>Areas Covered</a><a>Services</a><a>Testimonials</a><a>Contact</a><a>Fun Stuff</a>
</nav>

<h1 class="page-title display">About Us</h1>
<p class="page-sub display">"Your Children's and Family's Entertainment Specialist"</p>
<div class="stage-photo" role="img" aria-label="Photo of five entertainers posing on a stage in front of red curtains"></div>

<section class="about-copy">
  <p>Quindle has been performing professionally in the New York tri-state and Staten Island area since 1996 and has brought his special magic and memories to children's parties year after year and his popularity continues to grow with every fun and magical performance. As an experienced performer, Quindle knows how to thrill and entertain each audience member with age appropriate magic and humor to the delight of every party goer, both young and old! Quindle has won multiple awards and accolades for his performances as a clown and magician. He performs in every imaginable arena, from Back Yard parties,</p>
  <p>Theme parks and even the Harborline Film Festival. Besides being the most sought after entertainer in New York, Brooklyn, Staten Island and New Jersey, Quindle is also well recognized from his appearances on television, in magazines, and art gallery exhibits. He truly offers the best in children's magic, carnival and circus entertainment for every age, occasion and venue. He is an expert in all forms of magic, stage illusions, balloon sculpting, face painting, juggling and stilt walking. He has even delved into the realm of ventriloquism, and is ever expanding his broad range of party entertainment.</p>
  <p>Quindle's Play Barn started out in 2006 as an idea and philosophy about changing the children's entertainment industry. We quickly developed into something much bigger thanks to our reputation for providing the very best in children's parties and special event entertainment. We have now expanded into corporate events, Sweet 16's, Charity fundraisers, Bar and Bat Mitzvahs, School Shows, Carnivals, Weddings and much more. Our roster of talent includes some of the entertainment industry's top Magicians, Clowns, Balloon Sculptors, Face Painters, Jugglers and DJ's. They have helped to make and to keep Quindle's Play Barn a household name. Quindle's Play Barn specializes in children and family entertainment, making your</p>
</section>

<aside class="contact-panel">
  <h2 class="display">Contact Us</h2>
  <div class="field">Name</div>
  <div class="field">E-mail</div>
  <div class="field">Phone Number</div>
  <div class="field area">Enquiry</div>
  <div class="submit display">Submit</div>
</aside>

<div class="social">
  <div class="social-item"><span class="dot"></span>Pageface</div>
  <div class="social-item"><span class="dot"></span>Chirpline</div>
  <div class="social-item"><span class="dot"></span>Workring</div>
  <div class="social-item"><span class="dot"></span>Vidstream</div>
</div>

<footer class="site-footer">
  <div class="item" style="left:72px">
    <svg width="42" height="30" viewBox="0 0 42 30"><path d="M3 10 Q21 -2 39 10 L35 16 L28 12 L28 8 Q21 5 14 8 L14 12 L7 16 Z" fill="#fff"/><rect x="10" y="16" width="22" height="12" rx="3" fill="#fff"/></svg>
    555-014-2277</div>
  <div class="item" style="left:296px">
    <svg width="36" height="26" viewBox="0 0 36 26"><rect x="2" y="2" width="32" height="22" fill="none" stroke="#fff" stroke-width="2.5"/><path d="M2 2 L18 15 L34 2" fill="none" stroke="#fff" stroke-width="2.5"/></svg>
    info@quindlesplaybarn.com</div>
  <div class="item" style="left:642px">© 2014 Quindles Play Barn</div>
  <div class="item" style="left:939px">Sitemap</div>
  <div class="item" style="left:1064px">FAQ</div>
</footer>

</body>
</html>
```